Yoga for Scoliosis business card/logo design

I need a business card/logo design for my new business. I am a registered yoga teacher and am certified in yoga for scoliosis. I'd like my card to read "Marlow Yoga Yoga for a Healthy Spine" and would like to incorporate one of the letters in my name{ ie the first vertical line of the letter " H "or "D"} to resemble a scoliotic spine. I regularly teach the following:Yoga for Scoliosis, Yoga for Back Health, Hatha yoga, Vinyasa yoga with Iyengar style alignment. This business is mostly for private clients, but I also teach group, semi-private & work shop classes. I like the colors green (light emerald) and royal blue. I'd like the design to be somewhat sleek, but not too modern. I also like the idea of a ying/yang symbol with a scoliotic spine dviding it.

Danielle Marlow
200 RYT, Certified Yoga for Scoliosis Instructor
MarlowYoga.example
MarlowYoga@mailbox.example
555-412-3097

```html
<!DOCTYPE html>
<html lang="en">
<head>
<meta charset="utf-8">
<title>Marlow Yoga – Business Card</title>
<link rel="stylesheet" href="https://fonts.googleapis.com/css2?family=Arimo:wght@400&display=swap">
<style>
  :root {
    --stage: #a553b6;
    --card-light: #f4f1f8;
    --card-pink: #ecd3ea;
    --ink: #111111;
    --ink-soft: #4a4a4a;
    --brand-purple: #7c2a8c;
    --band-gray: #505050;
    --white: #ffffff;
    --photo-top: #f1dcef;
    --photo-mid: #bdb9bd;
    --photo-dark: #2a2a2a;
  }
  * { margin: 0; padding: 0; box-sizing: border-box; }
  html, body {
    width: 1200px;
    height: 902px;
    overflow: hidden;
    background: var(--stage);
    font-family: "Arimo", Arial, sans-serif;
  }
  .card {
    position: absolute;
    left: 50px;
    top: 137px;
    width: 1100px;
    height: 628px;
    overflow: hidden;
    background:
      radial-gradient(circle at 72% 60%, var(--card-pink) 0%, var(--card-light) 55%, #e9e6f1 100%);
  }
  .brand-name {
    position: absolute;
    left: 50px;
    top: 68px;
    font-size: 74px;
    font-weight: 400;
    color: var(--ink);
    letter-spacing: 0.5px;
    line-height: 1;
  }
  .tagline {
    position: absolute;
    left: 56px;
    top: 142px;
    font-size: 37px;
    color: var(--ink-soft);
    line-height: 1;
  }
  .person-name {
    position: absolute;
    left: 52px;
    top: 263px;
    font-size: 45px;
    color: var(--brand-purple);
    line-height: 1;
  }
  .credential {
    position: absolute;
    left: 55px;
    top: 324px;
    font-size: 25px;
    color: var(--ink-soft);
    line-height: 1;
  }
  .contact-list {
    position: absolute;
    left: 52px;
    top: 404px;
    list-style: none;
  }
  .contact-item {
    display: flex;
    align-items: center;
    height: 41px;
    font-size: 29px;
    color: var(--ink-soft);
  }
  .contact-icon {
    width: 31px;
    height: 31px;
    margin-right: 29px;
    flex: none;
  }
  .pose-photo {
    position: absolute;
    left: 576px;
    top: 131px;
    width: 480px;
    height: 420px;
    border-radius: 40% 40% 12% 12%;
    background:
      radial-gradient(ellipse at 50% 45%, var(--photo-dark) 0%, var(--photo-mid) 45%, var(--photo-top) 75%, transparent 100%);
    opacity: 0.85;
  }
  .footer-band {
    position: absolute;
    left: 0;
    bottom: 0;
    width: 1100px;
    height: 53px;
  }
</style>
</head>
<body>
  <main class="card">
    <h1 class="brand-name">Marlow Yoga</h1>
    <p class="tagline">Yoga for a Healthy Spine</p>

    <h2 class="person-name">Danielle Marlow</h2>
    <p class="credential">200 RYT, Certified Yoga for Scoliosis Instructor</p>

    <ul class="contact-list">
      <li class="contact-item">
        <svg class="contact-icon" viewBox="0 0 31 31" aria-hidden="true">
          <rect width="31" height="31" fill="var(--brand-purple)"/>
          <circle cx="15.5" cy="11" r="5" fill="var(--white)"/>
          <path d="M6 25 C6 18 25 18 25 25 Z" fill="var(--white)"/>
        </svg>
        555-412-3097
      </li>
      <li class="contact-item">
        <svg class="contact-icon" viewBox="0 0 31 31" aria-hidden="true">
          <rect width="31" height="31" fill="var(--brand-purple)"/>
          <circle cx="15.5" cy="15.5" r="9" fill="none" stroke="var(--white)" stroke-width="2"/>
          <ellipse cx="15.5" cy="15.5" rx="4" ry="9" fill="none" stroke="var(--white)" stroke-width="1.6"/>
          <line x1="6.5" y1="15.5" x2="24.5" y2="15.5" stroke="var(--white)" stroke-width="1.6"/>
        </svg>
        MarlowYoga.example
      </li>
      <li class="contact-item">
        <svg class="contact-icon" viewBox="0 0 31 31" aria-hidden="true">
          <rect width="31" height="31" fill="var(--brand-purple)"/>
          <rect x="6" y="9" width="19" height="13" fill="none" stroke="var(--white)" stroke-width="2"/>
          <path d="M6 9 L15.5 17 L25 9 M6 22 L13 15 M25 22 L18 15" fill="none" stroke="var(--white)" stroke-width="1.6"/>
        </svg>
        MarlowYoga@mailbox.example
      </li>
    </ul>

    <div class="pose-photo" role="img" aria-label="Photo of a yoga instructor in black top and grey leggings holding a seated backbend pose"></div>

    <svg class="footer-band" viewBox="0 0 1100 53" aria-hidden="true">
      <rect width="1100" height="53" fill="var(--brand-purple)"/>
      <polygon points="0,16 505,16 521,53 0,53" fill="var(--white)"/>
      <polygon points="0,22 499,22 512,53 0,53" fill="var(--band-gray)"/>
    </svg>
  </main>
</body>
</html>
```